Flyer Design

we need a flyer designing for our independent estate and letting agents based in Gosport Hampshire, our company name is Farrow and Partners Gosport, our contact details are 37 Willowmere Lane, Gosport, Hampshire PO13 4TJ, 02392 784630, email :tamsin@farrowpartners-example.co.uk. Our special offer we'd like to advertise is for the year 2015 we aim to sell 100 properties and only charge £1000 no vat sellers fee for each property sold. We are also offering a free no obligation market appraisal by one of our professional assessors. The flyer must have this disclaimer added to the bottom of it: if you are currently on the market with another agent then your current terms and conditions may need to be reviewed prior to changing agency. We advertise on Homevista and would like to see designs that use the colours lime green and navy blue. The final design should be eye catching and promote this special offer.

```html
<!DOCTYPE html>
<html lang="en">
<head>
<meta charset="utf-8">
<title>Farrow and Partners – 2015 Sellers Offer</title>
<link href="https://fonts.googleapis.com/css2?family=Tinos:wght@400;700&family=Open+Sans:wght@600;700;800&display=swap" rel="stylesheet">
<style>
  :root {
    --navy: #15213f;
    --lime: #a4c83c;
    --lime-light: #d3e69a;
    --white: #ffffff;
    --rule: #8a8f99;
  }
  * { margin: 0; padding: 0; box-sizing: border-box; }
  html, body { width: 850px; height: 1200px; overflow: hidden; background: var(--white); }
  .flyer { position: relative; width: 850px; height: 1200px; overflow: hidden; background: var(--white); font-family: "Open Sans", Arial, sans-serif; color: var(--navy); }

  .masthead { position: absolute; left: 0; top: 0; width: 850px; height: 150px; background: var(--navy); }
  .brand { position: absolute; left: 28px; top: 22px; color: var(--white); font-family: "Tinos", "Times New Roman", serif; }
  .brand-name { display: flex; align-items: center; gap: 12px; font-size: 38px; font-weight: 400; line-height: 1; }
  .brand-mark { width: 14px; height: 14px; background: var(--white); }
  .brand-tagline { margin-top: 14px; font-size: 13px; letter-spacing: 3px; text-transform: uppercase; padding-left: 26px; }
  .brand-address { margin-top: 12px; font-size: 13px; padding-left: 26px; }
  .contact { position: absolute; right: 28px; top: 22px; text-align: right; color: var(--white); }
  .contact-phone { font-family: "Tinos", "Times New Roman", serif; font-weight: 700; font-size: 40px; line-height: 1; }
  .contact-email { font-family: "Tinos", "Times New Roman", serif; font-weight: 700; font-size: 20px; line-height: 1.45; margin-top: 10px; }
  .contact-email + .contact-email { margin-top: 0; }

  .showcase { position: absolute; left: 0; top: 150px; width: 850px; height: 470px; }

  .intro { position: absolute; left: 0; top: 618px; width: 850px; height: 202px; background: var(--lime-light); }
  .intro-tabs { position: absolute; left: 190px; top: 4px; width: 530px; height: 34px; background: var(--white); display: flex; }
  .intro-tab { flex: 1; text-align: center; font-weight: 800; font-size: 19px; line-height: 34px; letter-spacing: 0.5px; }
  .intro-copy { position: absolute; top: 46px; font-weight: 700; font-size: 16px; line-height: 1.25; }
  .intro-copy--who { left: 40px; width: 382px; text-align: right; }
  .intro-copy--why { left: 452px; width: 376px; text-align: left; }

  .offer { position: absolute; left: 0; top: 820px; width: 850px; height: 290px; display: flex; }
  .offer-item { flex: 1; text-align: center; padding-top: 20px; }
  .offer-title { font-family: "Tinos", "Times New Roman", serif; font-weight: 700; font-size: 31px; line-height: 1; }
  .offer-figure { font-family: "Tinos", "Times New Roman", serif; font-weight: 400; font-size: 150px; line-height: 1; color: var(--lime); margin-top: 6px; }
  .offer-caption { font-family: "Tinos", "Times New Roman", serif; font-weight: 700; font-size: 26px; line-height: 1; margin-top: 4px; }
  .offer-divider { position: absolute; left: 424px; top: 18px; width: 2px; height: 222px; background: var(--rule); }
  .offer-appraisal { position: absolute; left: 0; top: 254px; width: 850px; text-align: center; font-weight: 800; font-size: 16px; line-height: 1.2; }

  .footer { position: absolute; left: 0; top: 1110px; width: 850px; height: 90px; background: var(--navy); color: var(--white); }
  .footer-phone { position: absolute; left: 56px; top: 22px; font-family: "Tinos", "Times New Roman", serif; font-weight: 700; font-size: 44px; line-height: 1; }
  .footer-disclaimer { position: absolute; right: 24px; top: 26px; width: 330px; text-align: right; font-family: "Tinos", "Times New Roman", serif; font-weight: 700; font-size: 12.5px; line-height: 1.25; }
</style>
</head>
<body>
<div class="flyer">
  <header class="masthead">
    <div class="brand">
      <div class="brand-name"><span class="brand-mark"></span>Farrow and Partners</div>
      <div class="brand-tagline">Estate &amp; Letting Agents</div>
      <div class="brand-address">37 Willowmere Lane, Gosport, Hampshire PO13 4TJ</div>
    </div>
    <div class="contact">
      <div class="contact-phone">02392 784630</div>
      <div class="contact-email">tamsin@farrowpartners-example.co.uk</div>
      <div class="contact-email">ellis@farrowpartners-example.co.uk</div>
    </div>
  </header>

  <svg class="showcase" viewBox="0 0 850 470" width="850" height="470">
    <defs>
      <linearGradient id="band" x1="0" y1="0" x2="0" y2="1">
        <stop offset="0" stop-color="#ffffff"/>
        <stop offset="0.35" stop-color="#e3efb8"/>
        <stop offset="1" stop-color="#a4c83c"/>
      </linearGradient>
      <linearGradient id="moving" x1="0" y1="0" x2="1" y2="1">
        <stop offset="0" stop-color="#e9dcc4"/>
        <stop offset="1" stop-color="#b79c74"/>
      </linearGradient>
      <linearGradient id="keys" x1="0" y1="0" x2="1" y2="1">
        <stop offset="0" stop-color="#6e6e70"/>
        <stop offset="1" stop-color="#1d1d22"/>
      </linearGradient>
      <linearGradient id="sign" x1="0" y1="0" x2="0" y2="1">
        <stop offset="0" stop-color="#e7e2dc"/>
        <stop offset="1" stop-color="#c73a36"/>
      </linearGradient>
    </defs>
    <rect x="0" y="0" width="850" height="470" fill="url(#band)"/>
    <path d="M0 330 Q425 250 850 330 L850 470 L0 470 Z" fill="#a4c83c"/>
    <circle cx="720" cy="225" r="212" fill="#ffffff"/>
    <circle cx="720" cy="225" r="200" fill="url(#sign)" role="img" aria-label="Photo of a red and white SOLD sign outside a home"/>
    <circle cx="140" cy="225" r="230" fill="#a4c83c"/>
    <circle cx="140" cy="225" r="216" fill="url(#moving)" role="img" aria-label="Photo of a child holding a teddy bear among moving boxes"/>
    <circle cx="425" cy="222" r="200" fill="#a4c83c"/>
    <circle cx="425" cy="222" r="186" fill="url(#keys)" role="img" aria-label="Photo of a hand holding out a set of house keys"/>
  </svg>

  <section class="intro">
    <div class="intro-tabs">
      <h2 class="intro-tab">WHO WE ARE</h2>
      <h2 class="intro-tab">WHY CHOOSE US</h2>
    </div>
    <p class="intro-copy intro-copy--who">Farrow and Partners are Independent Residential Estate and Letting Agents specialising in the effective and successful marketing of residential property in both the Gosport and surrounding areas. We have extensive experience in the estate agency industry and know this market well.</p>
    <p class="intro-copy intro-copy--why">We recognise that providing quality of service is the key to our success. It is a source of great satisfaction that so much of our business comes by way of recommendations from our many satisfied clients. We are extremely proud of our reputation and strive, not only to meet our clients' expectations, but to exceed them!</p>
  </section>

  <section class="offer">
    <div class="offer-item">
      <h3 class="offer-title">Our GOAL for 2015</h3>
      <div class="offer-figure">100</div>
      <div class="offer-caption">Homes SOLD</div>
    </div>
    <div class="offer-divider"></div>
    <div class="offer-item">
      <h3 class="offer-title">Our PRICE for 2015</h3>
      <div class="offer-figure">£1000</div>
      <div class="offer-caption">Sellers Fee no VAT</div>
    </div>
    <p class="offer-appraisal">FREE no obligation market appraisal by one of our professional assessors</p>
  </section>

  <footer class="footer">
    <div class="footer-phone">02392 784630</div>
    <p class="footer-disclaimer">If you are currently on the market with another agent then your current terms and conditions may need to be reviewed prior to changing agency.</p>
  </footer>
</div>
</body>
</html>
```